Private Security Company Business Card and Logo Design

Looking for a modern conservative business card design for our new private security company Harbor Ridge Guard Co., Inc. or HRGC for short.
Private Security Services. The current logo we have is not very good and honestly would like a sharp logo for the card instead of using the one we have now. Open to ideas. I am easy just looking for something nicer then what I can personally design on cardmillo. I searched on zintoo for Security Company business cards went to images and found some nice designs that were made here.

Target Market(s)

Security Services

Industry/Entity Type

Business

Contact Information for Business Card

Harbor Ridge Guard Co., Inc.
President, cell,office,fax,email, website,
Logo etc, whatever is needed for a standard business card
Can provide personal Information later.

Colors
0556a4
ffffff
474747

Requirements
Must have
• Modern but conservative,
Nice to have
• color choices
• Blue, white, Grey

```html
<!DOCTYPE html>
<html lang="en">
<head>
<meta charset="utf-8">
<title>Harbor Ridge Guard Co. — Business Card</title>
<link rel="stylesheet" href="https://fonts.googleapis.com/css2?family=Open+Sans:wght@400;600;700&family=Open+Sans+Condensed:wght@700&display=swap">
<style>
  :root {
    --brand-blue: #0556a4;
    --bright-blue: #1a7bd0;
    --charcoal: #474747;
    --paper: #ffffff;
    --paper-shade: #e9eaec;
    --stage: #ecebe8;
    --ink-soft: #5a5a5a;
  }
  * { box-sizing: border-box; margin: 0; padding: 0; }
  html, body { width: 1200px; height: 1023px; overflow: hidden; }
  body {
    background: var(--stage);
    font-family: "Open Sans", Arial, sans-serif;
    position: relative;
  }
  .card {
    position: absolute;
    left: 300px;
    width: 600px;
    height: 343px;
    border-radius: 16px;
    overflow: hidden;
    box-shadow: 0 6px 18px rgba(0,0,0,.18);
  }
  .card-front { top: 130px; background: var(--paper); }
  .card-back {
    top: 523px;
    background: linear-gradient(135deg, var(--paper) 0%, var(--paper-shade) 100%);
  }
  .card-art { position: absolute; inset: 0; }

  /* front */
  .front-mark {
    position: absolute; left: 150px; top: 118px;
    display: flex; align-items: center; gap: 12px;
  }
  .mark-dot {
    width: 22px; height: 22px; border-radius: 50%;
    background: var(--bright-blue);
  }
  .mark-name {
    font-weight: 700; font-size: 46px; letter-spacing: 2px;
    color: var(--paper);
  }
  .front-tagline {
    position: absolute; left: 150px; top: 186px;
    font-family: "Open Sans Condensed", "Open Sans", sans-serif;
    font-weight: 700; font-size: 22px; color: var(--paper);
  }
  .front-web {
    position: absolute; left: 550px; top: 171px;
    transform: translate(-50%, -50%) rotate(-90deg);
    font-size: 17px; letter-spacing: 3px; color: var(--ink-soft);
    white-space: nowrap;
  }

  /* back */
  .back-company {
    position: absolute; left: 48px; top: 30px;
    font-family: "Open Sans Condensed", "Open Sans", sans-serif;
    font-weight: 700; font-size: 27px; color: var(--brand-blue);
  }
  .back-mark {
    position: absolute; left: 300px; top: 92px;
    transform: translateX(-50%);
    display: flex; align-items: center; gap: 10px;
  }
  .back-mark .mark-dot { background: var(--brand-blue); width: 18px; height: 18px; }
  .back-mark .mark-name { color: var(--brand-blue); font-size: 40px; }
  .back-rule {
    position: absolute; left: 150px; top: 172px; width: 300px; height: 2px;
    background: linear-gradient(90deg, transparent, var(--brand-blue) 50%, transparent);
  }
  .contact-list {
    position: absolute; left: 170px; top: 190px;
    list-style: none; font-size: 14px; line-height: 21px; color: var(--brand-blue);
  }
  .contact-list li { display: flex; align-items: center; gap: 10px; white-space: nowrap; }
  .contact-list svg { width: 13px; height: 13px; fill: var(--charcoal); flex: none; }
  .back-person {
    position: absolute; right: 40px; bottom: 22px; text-align: left;
  }
  .person-name {
    font-family: "Open Sans Condensed", "Open Sans", sans-serif;
    font-weight: 700; font-size: 28px; color: var(--brand-blue); line-height: 1.1;
  }
  .person-role { font-size: 12px; color: var(--ink-soft); }
</style>
</head>
<body>

<section class="card card-front" aria-label="Card front">
  <svg class="card-art" viewBox="0 0 600 343" preserveAspectRatio="none" aria-hidden="true">
    <defs>
      <linearGradient id="panelShade" x1="0" y1="0" x2="1" y2="1">
        <stop offset="0" stop-color="#6b6d72"/>
        <stop offset="1" stop-color="#3a3c40"/>
      </linearGradient>
    </defs>
    <path d="M430 0 H600 V30 H470 Q440 30 430 0 Z" fill="var(--bright-blue)"/>
    <path d="M0 280 H70 Q110 280 122 343 H0 Z" fill="var(--bright-blue)"/>
    <path d="M0 0 H430 Q440 30 470 30 Q490 30 490 60 V270 Q490 300 460 300 H100 Q75 300 70 280 H0 Z" fill="url(#panelShade)"/>
  </svg>
  <div class="front-mark">
    <span class="mark-dot"></span>
    <span class="mark-name">HRGC</span>
  </div>
  <p class="front-tagline">Harbor Ridge Guard</p>
  <p class="front-web">www.hrgcsecurity.com</p>
</section>

<section class="card card-back" aria-label="Card back">
  <svg class="card-art" viewBox="0 0 600 343" preserveAspectRatio="none" aria-hidden="true">
    <rect x="0" y="0" width="8" height="343" fill="var(--brand-blue)"/>
    <rect x="592" y="0" width="8" height="343" fill="var(--brand-blue)"/>
  </svg>
  <p class="back-company">Harbor Ridge Guard Co., Inc.</p>
  <div class="back-mark">
    <span class="mark-dot"></span>
    <span class="mark-name">HRGC</span>
  </div>
  <div class="back-rule"></div>
  <ul class="contact-list">
    <li><svg viewBox="0 0 16 16"><rect x="4" y="1" width="8" height="14" rx="1.5"/></svg>55-210-47813</li>
    <li><svg viewBox="0 0 16 16"><path d="M2 5 Q8 1 14 5 L12 8 L10 6 H6 L4 8 Z M4 9 H12 V14 H4 Z"/></svg>55-210-47920</li>
    <li><svg viewBox="0 0 16 16"><rect x="2" y="6" width="12" height="8" rx="1"/><rect x="4" y="2" width="8" height="5"/></svg>55-210-47964</li>
    <li><svg viewBox="0 0 16 16"><path d="M1 3 H15 V13 H1 Z M1 3 L8 9 L15 3" stroke="#fff" stroke-width="1"/></svg>info@hrgcsecurity.com</li>
    <li><svg viewBox="0 0 16 16"><circle cx="8" cy="8" r="7"/></svg>www.hrgcsecurity.com</li>
  </ul>
  <div class="back-person">
    <p class="person-name">Your Name</p>
    <p class="person-role">President</p>
  </div>
</section>

</body>
</html>
```